Marlow Vantage - Health, Wellness, Fitness Consultants

Marlow Vantage are Marlow Vantage are leading consultants to the Health, Wellness and Fitness industry​​, with over 25 years experience working with some of the biggest global worldwide brands from equipment providers and facility operators to mass participation events and obstacle course races. Marlow Vantage is a multi disciplined business specialising in helping brands grow through insight, strategy creation and valuable sector collaboration, We are the official exclusive distributors of Kinfor Rig bodyweight training products for the UK and Ireland, Official Partners of Obstacle Course Race and Adventure Racing Brindle Dash & Cobalt Trek Tour - I would like a black background card, 1 side Marlow Vantage logo only other side Official, Exclusive, Distributors and Partners in the UK & Ireland. Then list Brindle Dash, Kinfor Rig, Cobalt Trek Tour contact details at very bottom Founder / Director - Perry Dunmore
Mobile - +44(0)7900123456
E - Mail - perry.dunmore@marlowvantage.example
Web - www.marlowvantage.example
Skype - marlowvantage

```html
<!DOCTYPE html>
<html lang="en">
<head>
<meta charset="utf-8">
<title>Marlow Vantage – Business Card</title>
<link rel="stylesheet" href="https://fonts.googleapis.com/css2?family=Lato:wght@300;400;700;900&family=Tinos&display=swap">
<style>
  :root{
    --stage:#3b3b3b;
    --card-black:#161616;
    --card-white:#f2f2f2;
    --ink:#222222;
    --orange:#ef7b1a;
    --lime:#b6c95a;
    --gold:#b8953f;
    --blue:#1a86c8;
    --white:#ffffff;
  }
  *{box-sizing:border-box;margin:0;padding:0}
  html,body{width:799px;height:1200px;overflow:hidden;background:var(--stage)}
  .canvas{position:relative;width:799px;height:1200px}
  .card{position:absolute;left:80px;width:640px;height:366px;overflow:hidden;box-shadow:0 10px 24px rgba(0,0,0,.45)}
  .card--front{top:150px;background:var(--card-black)}
  .card--back{top:680px;background:var(--card-white)}

  .brand-mark{position:absolute;left:0;right:0;top:120px;text-align:center;font-family:"Tinos",serif}
  .brand-mark__name{font-size:58px;color:var(--lime);line-height:1}
  .brand-mark__tagline{margin-top:26px;font-size:20px;color:var(--gold);letter-spacing:.5px}

  .back-wave{position:absolute;inset:0;width:640px;height:366px}
  .company{position:absolute;left:40px;top:64px;font-family:"Lato",sans-serif;color:var(--ink)}
  .company__name{font-weight:300;font-size:40px;line-height:1}
  .company__tagline{font-weight:400;font-size:13px;margin-top:6px}
  .contacts{position:absolute;left:40px;top:140px;list-style:none;font-family:"Lato",sans-serif;font-size:13px;color:var(--ink)}
  .contacts li{display:flex;align-items:center;gap:8px;height:20px}
  .contacts svg{width:12px;height:12px;fill:var(--ink)}
  .person{position:absolute;right:36px;top:78px;text-align:left;font-family:"Lato",sans-serif;color:var(--white)}
  .person__name{font-weight:900;font-size:20px;letter-spacing:.5px;line-height:1.2}
  .person__role{font-weight:400;font-size:13px;margin-top:2px}
  .partners{position:absolute;left:40px;right:40px;top:292px;display:flex;align-items:center;justify-content:space-between;font-family:"Lato",sans-serif;font-weight:900;font-size:26px}
  .partner--rig{color:var(--blue)}
  .partner--dash{color:var(--ink)}
  .partner--trek{color:var(--orange);display:flex;align-items:center;gap:8px;font-size:20px}
  .partner__dot{width:24px;height:24px;border-radius:50%;background:var(--ink)}
</style>
</head>
<body>
<main class="canvas">
  <section class="card card--front" aria-label="Card front">
    <div class="brand-mark">
      <div class="brand-mark__name">Marlow Vantage</div>
      <div class="brand-mark__tagline">Health | Wellness | Fitness | Consultants</div>
    </div>
  </section>

  <section class="card card--back" aria-label="Card back">
    <svg class="back-wave" viewBox="0 0 640 366" aria-hidden="true">
      <path d="M0,0 H640 V262 C590,262 550,245 500,210 C450,175 420,100 360,60 C300,25 150,18 0,18 Z" fill="var(--card-black)"/>
      <path d="M0,24 C150,24 290,30 350,62 C380,80 395,95 405,110" fill="none" stroke="var(--orange)" stroke-width="6"/>
      <path d="M60,34 C180,34 300,42 358,74 C420,112 450,188 500,222 C550,256 590,272 640,272" fill="none" stroke="var(--lime)" stroke-width="5"/>
    </svg>

    <div class="company">
      <div class="company__name">Marlow Vantage</div>
      <div class="company__tagline">Health, Wellness, Fitness, Consultants</div>
    </div>

    <ul class="contacts">
      <li><svg viewBox="0 0 12 12"><path d="M2 1h3l1 3-2 1a7 7 0 0 0 3 3l1-2 3 1v3c-6 0-10-4-10-9z"/></svg>+44(0)7900123456</li>
      <li><svg viewBox="0 0 12 12"><path d="M0 2h12v8H0z M1 3l5 4 5-4" fill="none" stroke="#222" stroke-width="1.2"/></svg>perry.dunmore@marlowvantage.example</li>
      <li><svg viewBox="0 0 12 12"><circle cx="6" cy="6" r="5" fill="none" stroke="#222" stroke-width="1.2"/><path d="M1 6h10M6 1c-3 3-3 7 0 10M6 1c3 3 3 7 0 10" fill="none" stroke="#222" stroke-width="1"/></svg>www.marlowvantage.example</li>
      <li><svg viewBox="0 0 12 12"><circle cx="6" cy="6" r="5"/></svg>marlowvantage</li>
    </ul>

    <div class="person">
      <div class="person__name">PERRY DUNMORE</div>
      <div class="person__role">Founder / Director</div>
    </div>

    <div class="partners">
      <span class="partner partner--rig">Kinfor Rig</span>
      <span class="partner partner--dash">Brindle Dash</span>
      <span class="partner partner--trek"><span class="partner__dot"></span>Cobalt Trek Tour</span>
    </div>
  </section>
</main>
</body>
</html>
```